Veltarum

Standard Business Card design.
Sample two-sided design uploaded. White front, Black back.
Would like white shield to be on all black background side.
Willing to look at a couple creative designs, but nothing crazy.
Preference for a classic, confident, strong design.

```html
<!DOCTYPE html>
<html lang="en">
<head>
<meta charset="utf-8">
<title>Veltarum Business Card</title>
<link href="https://fonts.googleapis.com/css2?family=Open+Sans:wght@400;600;700&display=swap" rel="stylesheet">
<style>
  :root {
    --stage: #232323;
    --card: #1c1c1f;
    --card-edge: #2a2a2e;
    --ink: #ffffff;
    --ink-soft: #e6e6e6;
    --emboss-dark: #141416;
    --emboss-light: #3a3a3e;
  }
  html, body {
    margin: 0;
    width: 1200px;
    height: 780px;
    overflow: hidden;
    background: var(--stage);
    font-family: "Open Sans", Arial, sans-serif;
  }
  .canvas {
    position: relative;
    width: 1200px;
    height: 780px;
  }
  .card {
    position: absolute;
    top: 235px;
    width: 540px;
    height: 309px;
    background: var(--card);
    border: 1px solid var(--card-edge);
    border-radius: 4px;
    overflow: hidden;
    box-shadow: 0 18px 40px rgba(0,0,0,0.45);
  }
  .card--front { left: 40px; }
  .card--back { left: 620px; }

  /* Front */
  .emboss-area {
    position: absolute;
    left: 0; top: 0;
    width: 260px; height: 100%;
    background: radial-gradient(circle at 60% 35%, var(--emboss-light) 0%, var(--card) 45%, var(--emboss-dark) 100%);
  }
  .front-info {
    position: absolute;
    right: 32px; top: 34px;
    text-align: right;
    color: var(--ink);
  }
  .brand {
    display: inline-flex;
    align-items: center;
    gap: 10px;
    font-weight: 600;
    color: var(--ink);
    letter-spacing: 0.12em;
  }
  .brand__mark {
    background: var(--ink);
    display: inline-block;
  }
  .brand--small { font-size: 22px; }
  .brand--small .brand__mark { width: 16px; height: 16px; }
  .person__name {
    margin: 22px 0 0;
    font-size: 24px;
    font-weight: 700;
  }
  .person__role {
    margin: 2px 0 14px;
    font-size: 13px;
    color: var(--ink-soft);
  }
  .address {
    margin: 0 0 12px;
    font-size: 12.5px;
    line-height: 1.45;
    color: var(--ink-soft);
    font-style: normal;
  }
  .contacts {
    list-style: none;
    margin: 0; padding: 0;
    font-size: 12.5px;
    line-height: 1.7;
    color: var(--ink-soft);
  }
  .contacts li {
    display: flex;
    justify-content: flex-end;
    align-items: center;
    gap: 8px;
  }
  .contacts svg { width: 12px; height: 12px; fill: none; stroke: var(--ink); stroke-width: 1.6; }

  /* Back */
  .pattern-area {
    position: absolute;
    inset: 0;
    background: linear-gradient(115deg, var(--card) 0%, #202024 55%, #2c2c30 80%, var(--card) 100%);
  }
  .back-center {
    position: absolute;
    inset: 0;
    display: flex;
    align-items: center;
    justify-content: center;
  }
  .brand--large { font-size: 38px; gap: 14px; }
  .brand--large .brand__mark { width: 26px; height: 26px; }
</style>
</head>
<body>
<main class="canvas">
  <section class="card card--front" aria-label="Card front">
    <div class="emboss-area" role="img" aria-label="Large embossed brand emblem in dark gloss"></div>
    <div class="front-info">
      <div class="brand brand--small"><span class="brand__mark"></span>VELTARUM</div>
      <p class="person__name">Elena Marsh</p>
      <p class="person__role">Co-Founder</p>
      <address class="address">4180 Crestline Ave. Suite 310<br>Arlington, TX 76011</address>
      <ul class="contacts">
        <li>(555) 214-6630
          <svg viewBox="0 0 24 24"><path d="M5 3h4l2 5-3 2a12 12 0 0 0 6 6l2-3 5 2v4a2 2 0 0 1-2 2A18 18 0 0 1 3 5a2 2 0 0 1 2-2z"/></svg>
        </li>
        <li>hello@veltarum.co
          <svg viewBox="0 0 24 24"><rect x="3" y="5" width="18" height="14" rx="1"/><path d="M3 6l9 7 9-7"/></svg>
        </li>
        <li>www.veltarum.co
          <svg viewBox="0 0 24 24"><circle cx="12" cy="12" r="9"/><path d="M3 12h18M12 3a14 14 0 0 1 0 18M12 3a14 14 0 0 0 0 18"/></svg>
        </li>
      </ul>
    </div>
  </section>

  <section class="card card--back" aria-label="Card back">
    <div class="pattern-area" role="img" aria-label="Repeating spot-gloss brand emblem pattern on black"></div>
    <div class="back-center">
      <div class="brand brand--large"><span class="brand__mark"></span>VELTARUM</div>
    </div>
  </section>
</main>
</body>
</html>
```